MossVane Spa, Skincare and Cosmetics website

I need a website for MossVane (putting the glow back into people's skin) which allows viewers to access information about Beauty Spa packaging and facilities as well as online skincare and cosmetic products. Our distinctive difference is that our products are certified organic. We want to target a luxury high income niche market (age 30-50). I want all colours to be "baby colours" preferably background to be "baby metallic pink" (but please don't make the website too immature) with curves as patterns. I want a romantic vintage look.

The website needs to look:
1. elegant (prestige and luxury)
2. bright (baby colours mainly)
3. European curves and signature patterns
4. Can include Pearl related pics (but not a must)

The website pages needs to have:
1. pages ordering skincare/cosmetics
2. shopping cart and payment
3. about us and about our product differences
4. contact us
5. booking for spa treatments and packages

I have attached our logo and also packaging label styles.

Industry/Entity Type

Cosmetics

```html
<!DOCTYPE html>
<html lang="en">
<head>
<meta charset="utf-8">
<title>MossVane Spa, Skincare and Cosmetics</title>
<link rel="stylesheet" href="https://fonts.googleapis.com/css2?family=Cinzel:wght@400&family=Questrial&family=Arimo:wght@400;700&display=swap">
<style>
  :root {
    --frame-pink: #f09a9e;
    --overlay-pink: #f3a8ad;
    --stripe-pink: #ec949b;
    --taupe: #d1b2a9;
    --blush: #f8cdd0;
    --ink: #2e2424;
    --magenta: #d2308a;
    --cream: #ece0da;
    --white: #ffffff;
  }
  * { margin: 0; padding: 0; box-sizing: border-box; }
  html, body { width: 1200px; height: 999px; overflow: hidden; }
  body { background: var(--frame-pink); position: relative; font-family: "Arimo", Arial, sans-serif; }

  .page {
    position: absolute; left: 53px; top: 91px;
    width: 1094px; height: 827px; overflow: hidden;
    background: var(--taupe);
  }
  .page-shapes { position: absolute; left: 0; top: 0; }

  .main-nav {
    position: absolute; left: 35px; top: 27px; width: 1030px;
    display: flex; justify-content: space-between;
    font-family: "Questrial", "Century Gothic", sans-serif;
    font-size: 13.2px; letter-spacing: 0.1px; color: var(--ink);
  }
  .main-nav a { color: inherit; text-decoration: none; white-space: nowrap; }
  .main-nav a.is-active { color: var(--magenta); }

  .brand-name {
    position: absolute; left: 70px; top: 200px;
    font-family: "Cinzel", serif; font-size: 44px; letter-spacing: 2px;
    color: var(--cream); line-height: 1;
  }
  .hero-intro {
    position: absolute; left: 72px; top: 254px; width: 281px;
    font-size: 12.4px; line-height: 13.6px; color: var(--white);
    text-align: justify; letter-spacing: 0.2px;
  }

  .feature { position: absolute; top: 527px; width: 150px; }
  .feature-photo {
    width: 144px; height: 144px; border-radius: 50%;
    border: 3px solid var(--stripe-pink); margin: 0 0 0 2px;
  }
  .feature-title {
    margin-top: 19px; text-align: center;
    font-size: 10px; font-weight: 700; line-height: 11px; color: var(--ink);
    letter-spacing: 0.3px;
  }
  .feature-title.is-active { color: var(--magenta); }
  .feature-text {
    margin-top: 13px; font-size: 6.6px; line-height: 7.6px; color: var(--ink);
  }
  .photo-products { background: radial-gradient(circle at 40% 45%, #f2e3a8, #a8b84e 45%, #5c7a2e 85%); }
  .photo-bottle { background: radial-gradient(circle at 55% 65%, #4fc2c4, #e4e6e2 40%, #f3f2ee 80%); }
  .photo-relax { background: radial-gradient(circle at 45% 55%, #e9c3aa, #f4ece6 45%, #d8eac6 90%); }
  .photo-citrus { background: radial-gradient(circle at 40% 60%, #f2c33a, #f09a2a 45%, #f5e8d8 90%); }
</style>
</head>
<body>
  <main class="page">
    <svg class="page-shapes" width="1094" height="827" viewBox="0 0 1094 827" aria-hidden="false">
      <defs>
        <linearGradient id="heroTone" x1="0" y1="0" x2="1" y2="0.3">
          <stop offset="0" stop-color="#5e2f24"/>
          <stop offset="0.28" stop-color="#a8614b"/>
          <stop offset="0.55" stop-color="#dca28e"/>
          <stop offset="0.85" stop-color="#ecd2ca"/>
          <stop offset="1" stop-color="#f2e4e0"/>
        </linearGradient>
      </defs>
      <path role="img" aria-label="Close-up portrait photograph of a woman with glowing skin"
            d="M0,0 H1094 V372 C980,430 880,520 760,512 C560,498 300,395 0,395 Z"
            fill="url(#heroTone)"/>
      <path class="hero-veil" d="M0,0 H1094 V80 C960,95 860,205 600,208 C380,210 220,92 0,88 Z"
            fill="var(--overlay-pink)" opacity="0.88"/>
      <path class="hero-stripe" d="M0,402 C300,402 560,505 760,520 C880,528 980,440 1094,382"
            fill="none" stroke="var(--stripe-pink)" stroke-width="7"/>
      <path class="footer-wave" d="M0,827 C80,730 160,676 250,674 C460,668 700,730 1094,796 V827 Z"
            fill="var(--blush)"/>
      <path class="footer-wave-line" d="M0,827 C80,730 160,676 250,674 C460,668 700,730 1094,796"
            fill="none" stroke="var(--stripe-pink)" stroke-width="4"/>
    </svg>

    <nav class="main-nav">
      <a href="#">ABOUT US</a>
      <a href="#">OUR PRODUCT</a>
      <a href="#" class="is-active">ORDERING SKINCARE/COSMETICS</a>
      <a href="#">SHOPPING CART</a>
      <a href="#">PAYMENT</a>
      <a href="#">BOOKING FOR SPA</a>
      <a href="#">TREATMENTS AND PACKAGES</a>
      <a href="#">CONTACT US</a>
    </nav>

    <h1 class="brand-name">MossVane</h1>
    <p class="hero-intro">MossVane This is your one stop destination for Skin Care Cosmetics you've been looking for. Available in all styles, including Coverup and Eyeliner. It does not matter what you're looking for we can help you find it with the lowest prices online only found here at MossVane Let us help you meet your shopping needs while providing you with the best selections</p>

    <section class="feature" style="left:199px">
      <div class="feature-photo photo-products" role="img" aria-label="Photograph of skincare bottles, candles and leaves"></div>
      <h2 class="feature-title is-active">ORDERING<br>SKINCARE/COSMETICS</h2>
      <p class="feature-text">MossVane This is your one stop destination for Skin Care Cosmetics you've been looking for. Available in all styles, including Coverup and Eyeliner. It does not matter what you're looking for we can help you find it with the lowest prices online only found here at MossVane Let us help you meet your shopping needs while providing you with the best selections</p>
    </section>

    <section class="feature" style="left:376px">
      <div class="feature-photo photo-bottle" role="img" aria-label="Photograph of a glass bottle of spa oil with white flowers"></div>
      <h2 class="feature-title">SHOPPING<br>CART</h2>
      <p class="feature-text">MossVane This is your one stop destination for Skin Care Cosmetics you've been looking for. Available in all styles, including Coverup and Eyeliner. It does not matter what you're looking for we can help you find it with the lowest prices online only found here at MossVane Let us help you meet your shopping needs while providing you with the best selections</p>
    </section>

    <section class="feature" style="left:577px">
      <div class="feature-photo photo-relax" role="img" aria-label="Photograph of a woman relaxing at a spa"></div>
      <h2 class="feature-title">BOOKING<br>SPA</h2>
      <p class="feature-text">MossVane This is your one stop destination for Skin Care Cosmetics you've been looking for. Available in all styles, including Coverup and Eyeliner. It does not matter what you're looking for we can help you find it with the lowest prices online only found here at MossVane Let us help you meet your shopping needs while providing you with the best selections</p>
    </section>

    <section class="feature" style="left:748px">
      <div class="feature-photo photo-citrus" role="img" aria-label="Photograph of bath salts in a jar with orange slices"></div>
      <h2 class="feature-title">TREATMENTS<br>AND PACKAGES</h2>
      <p class="feature-text">MossVane This is your one stop destination for Skin Care Cosmetics you've been looking for. Available in all styles, including Coverup and Eyeliner. It does not matter what you're looking for we can help you find it with the lowest prices online only found here at MossVane Let us help you meet your shopping needs while providing you with the best selections</p>
    </section>
  </main>
</body>
</html>
```